Spinning Wheel: Spin & Win

We are looking to design a large sticker cover for a spinning wheel (please see attached reference)

Wheel diameter: 120 cm (1.2meters)

Divided into 8 sections:
1- Free Meal
2- Tolvik Gift Card
3- Haircut or Blowdry
4- Tolvik Gift Card
5- Merchandise
6- Tolvik Gift Card
7- Meal voucher
8- Tolvik Gift Card

Text in the center:
Buy for 200 AED to Spin & Win!
(Spin & Win should be the most dominant visually)

Font: Something classy and elegant (maybe cursive but easily read)

Colors: Khaki - All shades of brown and dark brown (note: the wheel structure is made of wood that is dark brown)

Feel: Wood and Old Paper
Updates

Target Market(s)

Upper Class

Industry/Entity Type

Graphic Design

Font styles to use
Decorative
Script

Requirements
Should not have
• Flashy colors

```html
<!DOCTYPE html>
<html lang="en">
<head>
<meta charset="utf-8">
<title>Spin &amp; Win Prize Wheel</title>
<link rel="stylesheet" href="https://fonts.googleapis.com/css2?family=Federant&display=swap">
<style>
  :root {
    --page-bg: #ffffff;
    --wood-dark-1: #4a2412;
    --wood-dark-2: #6e3b1f;
    --wood-dark-3: #5a2d16;
    --wood-light-1: #d7a874;
    --wood-light-2: #b98450;
    --wood-light-3: #9c6636;
    --seam: #3a1a0b;
    --ink-dark: #6a2a10;
    --ink-light: #f3cd90;
    --hub-1: #9a5a2e;
    --hub-2: #5e2c12;
    --hub-rim: #c89a55;
    --gold-1: #fff0a6;
    --gold-2: #e2b845;
    --gold-3: #a8741c;
    --carving-1: #e9c79a;
    --carving-2: #a9774a;
  }
  html, body {
    margin: 0;
    padding: 0;
    width: 1200px;
    height: 1200px;
    overflow: hidden;
    background: var(--page-bg);
  }
  .prize-wheel {
    display: block;
    width: 1200px;
    height: 1200px;
  }
  .wedge--dark { fill: url(#woodDark); stroke: var(--seam); stroke-width: 2; }
  .wedge--light { fill: url(#woodLight); stroke: var(--seam); stroke-width: 2; }
  .prize-label {
    font-family: "Federant", serif;
    font-size: 38px;
    text-anchor: middle;
    letter-spacing: 1px;
  }
  .prize-label--on-dark { fill: var(--ink-light); }
  .prize-label--on-light { fill: var(--ink-dark); }
  .rim-flourish { fill: url(#goldSoft); }
  .hub-carving { fill: url(#carvingSoft); }
  .hub-disc { fill: url(#hubWood); stroke: var(--hub-rim); stroke-width: 4; }
  .hub-title {
    font-family: "Federant", serif;
    text-anchor: middle;
    fill: url(#goldText);
    stroke: #7a4f12;
    stroke-width: 1.5;
  }
  .hub-title--main { font-size: 96px; }
  .hub-title--amp { font-size: 36px; }
  .hub-offer {
    font-family: "Federant", serif;
    font-size: 22px;
    text-anchor: middle;
    letter-spacing: 0.5px;
    fill: var(--ink-light);
  }
</style>
</head>
<body>
<svg class="prize-wheel" viewBox="0 0 1200 1200" xmlns="http://www.w3.org/2000/svg">
  <defs>
    <radialGradient id="woodDark" cx="600" cy="600" r="588" gradientUnits="userSpaceOnUse">
      <stop offset="0.2" style="stop-color: var(--wood-dark-1)"/>
      <stop offset="0.6" style="stop-color: var(--wood-dark-2)"/>
      <stop offset="1" style="stop-color: var(--wood-dark-3)"/>
    </radialGradient>
    <radialGradient id="woodLight" cx="600" cy="600" r="588" gradientUnits="userSpaceOnUse">
      <stop offset="0.2" style="stop-color: var(--wood-light-1)"/>
      <stop offset="0.65" style="stop-color: var(--wood-light-2)"/>
      <stop offset="1" style="stop-color: var(--wood-light-3)"/>
    </radialGradient>
    <radialGradient id="goldSoft">
      <stop offset="0" style="stop-color: var(--gold-1)"/>
      <stop offset="0.55" style="stop-color: var(--gold-2)"/>
      <stop offset="1" style="stop-color: var(--gold-3); stop-opacity: 0.2"/>
    </radialGradient>
    <radialGradient id="carvingSoft">
      <stop offset="0.7" style="stop-color: var(--carving-1)"/>
      <stop offset="1" style="stop-color: var(--carving-2); stop-opacity: 0"/>
    </radialGradient>
    <radialGradient id="hubWood" cx="0.45" cy="0.4">
      <stop offset="0" style="stop-color: var(--hub-1)"/>
      <stop offset="1" style="stop-color: var(--hub-2)"/>
    </radialGradient>
    <linearGradient id="goldText" x1="0" y1="0" x2="0" y2="1">
      <stop offset="0" style="stop-color: var(--gold-1)"/>
      <stop offset="0.5" style="stop-color: var(--gold-2)"/>
      <stop offset="1" style="stop-color: var(--gold-3)"/>
    </linearGradient>
  </defs>

  <!-- Top: gift card -->
  <g class="wheel-section" transform="rotate(90 600 600)">
    <path class="wedge--dark" d="M600 600 L56.8 375 A588 588 0 0 0 56.8 825 Z"/>
    <text class="prize-label prize-label--on-dark" x="262" y="586">Tolvik</text>
    <text class="prize-label prize-label--on-dark" x="262" y="640">Gift Card</text>
    <ellipse class="rim-flourish" cx="78" cy="600" rx="34" ry="104" role="img" aria-label="Gold carved flourish"/>
  </g>

  <!-- Top right: free meal -->
  <g class="wheel-section" transform="rotate(135 600 600)">
    <path class="wedge--light" d="M600 600 L56.8 375 A588 588 0 0 0 56.8 825 Z"/>
    <text class="prize-label prize-label--on-light" x="262" y="586">Free</text>
    <text class="prize-label prize-label--on-light" x="262" y="640">Meal</text>
    <ellipse class="rim-flourish" cx="78" cy="600" rx="34" ry="104" role="img" aria-label="Gold carved flourish"/>
  </g>

  <!-- Right: gift card -->
  <g class="wheel-section" transform="rotate(180 600 600)">
    <path class="wedge--dark" d="M600 600 L56.8 375 A588 588 0 0 0 56.8 825 Z"/>
    <text class="prize-label prize-label--on-dark" x="262" y="586">Tolvik</text>
    <text class="prize-label prize-label--on-dark" x="262" y="640">Gift Card</text>
    <ellipse class="rim-flourish" cx="78" cy="600" rx="34" ry="104" role="img" aria-label="Gold carved flourish"/>
  </g>

  <!-- Bottom right: haircut -->
  <g class="wheel-section" transform="rotate(225 600 600)">
    <path class="wedge--light" d="M600 600 L56.8 375 A588 588 0 0 0 56.8 825 Z"/>
    <text class="prize-label prize-label--on-light" x="262" y="586">Haircut or</text>
    <text class="prize-label prize-label--on-light" x="262" y="640">Blowdry</text>
    <ellipse class="rim-flourish" cx="78" cy="600" rx="34" ry="104" role="img" aria-label="Gold carved flourish"/>
  </g>

  <!-- Bottom: gift card -->
  <g class="wheel-section" transform="rotate(270 600 600)">
    <path class="wedge--dark" d="M600 600 L56.8 375 A588 588 0 0 0 56.8 825 Z"/>
    <text class="prize-label prize-label--on-dark" x="262" y="586">Tolvik</text>
    <text class="prize-label prize-label--on-dark" x="262" y="640">Gift Card</text>
    <ellipse class="rim-flourish" cx="78" cy="600" rx="34" ry="104" role="img" aria-label="Gold carved flourish"/>
  </g>

  <!-- Bottom left: merchandise -->
  <g class="wheel-section" transform="rotate(315 600 600)">
    <path class="wedge--light" d="M600 600 L56.8 375 A588 588 0 0 0 56.8 825 Z"/>
    <text class="prize-label prize-label--on-light" x="262" y="613">Merchandise</text>
    <ellipse class="rim-flourish" cx="78" cy="600" rx="34" ry="104" role="img" aria-label="Gold carved flourish"/>
  </g>

  <!-- Left: gift card -->
  <g class="wheel-section" transform="rotate(0 600 600)">
    <path class="wedge--dark" d="M600 600 L56.8 375 A588 588 0 0 0 56.8 825 Z"/>
    <text class="prize-label prize-label--on-dark" x="262" y="586">Tolvik</text>
    <text class="prize-label prize-label--on-dark" x="262" y="640">Gift Card</text>
    <ellipse class="rim-flourish" cx="78" cy="600" rx="34" ry="104" role="img" aria-label="Gold carved flourish"/>
  </g>

  <!-- Top left: meal voucher -->
  <g class="wheel-section" transform="rotate(45 600 600)">
    <path class="wedge--light" d="M600 600 L56.8 375 A588 588 0 0 0 56.8 825 Z"/>
    <text class="prize-label prize-label--on-light" x="262" y="586">Meal</text>
    <text class="prize-label prize-label--on-light" x="262" y="640">Voucher</text>
    <ellipse class="rim-flourish" cx="78" cy="600" rx="34" ry="104" role="img" aria-label="Gold carved flourish"/>
  </g>

  <!-- Hub -->
  <g class="wheel-hub">
    <circle class="hub-carving" cx="600" cy="600" r="225" role="img" aria-label="Carved wooden leaf rosette around the hub"/>
    <circle class="hub-disc" cx="600" cy="600" r="168"/>
    <text class="hub-offer" x="600" y="496">Buy for 200 AED to</text>
    <text class="hub-title hub-title--main" x="600" y="585">Spin</text>
    <text class="hub-title hub-title--amp" x="600" y="628">&amp;</text>
    <text class="hub-title hub-title--main" x="600" y="712">Win!</text>
  </g>
</svg>
</body>
</html>
```